Sports and football Live scores website

Hey designers, I want a website which will feature live football and other sports events on demand and on the go. This website should be similar to http://pitchtally.example
As the football events are been played, my website will be giving live updates of the events. There will be different categories such as football, basket, tennis and others as the website above. Also, there will be menu for top footballing nations as also show in the website above. My website should refresh it's self every one minutes. The proposed live score website should be youthful and attractive. Bright colors such me used as my target audience are sports lovers.

```html
<!DOCTYPE html>
<html lang="en">
<head>
<meta charset="utf-8">
<title>Kickorra – Live Scores</title>
<link href="https://fonts.googleapis.com/css2?family=Roboto:wght@400;500;700;900&display=swap" rel="stylesheet">
<style>
:root{
  --orange:#f28c1c;
  --orange-dark:#e0760a;
  --green:#3f7d1c;
  --green-dark:#2c5a12;
  --social:#1f3d10;
  --ink:#333;
  --muted:#888;
  --line:#e3e3e3;
  --panel:#f5f5f5;
  --dark:#2f2f2f;
  --white:#fff;
}
*{box-sizing:border-box;margin:0;padding:0}
html,body{width:669px;height:1200px;overflow:hidden;background:var(--white);font-family:"Roboto",Arial,sans-serif;color:var(--ink)}
.page{position:relative;width:669px;height:1200px}

/* hero */
.hero{position:absolute;left:0;top:0;width:669px;height:298px;background:linear-gradient(135deg,#243a1a 0%,#4c6b3a 35%,#9aa49a 60%,#d8dcd8 80%,#5c7050 100%)}
.hero-photo{position:absolute;inset:0}
.topbar{position:absolute;left:0;top:0;width:100%;height:16px;background:rgba(20,40,10,.85);display:flex;gap:22px;padding-left:78px;align-items:center}
.topbar a{font-size:6px;color:var(--orange);text-decoration:none;font-weight:700;letter-spacing:.3px}
.header{position:absolute;top:26px;left:73px;width:525px;display:flex;align-items:center}
.logo{font-size:27px;font-weight:700;color:var(--white)}
.nav{display:flex;gap:14px;margin-left:30px;align-items:center}
.nav a{color:var(--white);font-size:7.5px;font-weight:700;text-decoration:none}
.hero-copy{position:absolute;left:73px;top:204px;color:var(--white)}
.hero-copy .kicker{font-size:15px;font-weight:500}
.hero-copy h1{font-size:23px;font-weight:900;line-height:1.05}
.btn{display:inline-block;margin-top:10px;background:var(--orange);color:var(--white);font-size:7px;font-weight:700;padding:6px 12px}
.hero-rule{position:absolute;left:73px;bottom:4px;width:525px;height:3px;background:var(--orange)}

/* main */
.main{position:absolute;top:330px;left:73px;width:525px;display:flex;gap:16px}
.scores{width:352px}
.section-title{font-size:12px;font-weight:900;border-bottom:2px solid var(--orange);padding-bottom:4px;margin-bottom:6px}
.tabs{display:flex;border:1px solid var(--line)}
.tabs span{flex:1;text-align:center;font-size:6px;padding:4px 0;color:var(--muted)}
.tabs .active{background:var(--green);color:var(--white)}
.group{border:1px solid var(--line);border-top:none}
.group .league{background:var(--panel);font-size:6.5px;height:20px;line-height:20px;padding:0 8px;color:#555}
.match,.srow{display:grid;grid-template-columns:34px 1fr 40px 1fr 16px;font-size:6px;align-items:center;padding:0 8px;color:#555}
.match{height:24px}
.match .home{text-align:right;padding-right:6px}
.score{text-align:center;font-weight:700}
.group-gap{height:30px}
.series{margin-top:22px}
.series-head{background:var(--dark);color:var(--white);font-size:7px;font-weight:700;padding:5px 8px}
.srow{height:17px;border-bottom:1px solid var(--line)}
.srow .home{text-align:right;padding-right:6px}
.dot{width:8px;height:8px;border-radius:50%;border:1.5px solid var(--orange)}
.more{display:flex;justify-content:center;margin-top:10px}

/* sidebar */
.sidebar{width:157px;padding-top:16px}
.widget-head{font-size:7.5px;font-weight:700;color:var(--white);padding:6px 8px}
.live-table{background:var(--orange)}
.live-table .widget-head{background:var(--orange-dark)}
.live-table .search{margin:5px 6px;height:11px;background:var(--white);font-size:5.5px;color:var(--muted);padding:2px 4px}
.live-row{display:flex;justify-content:space-between;font-size:6px;color:var(--white);padding:6px 8px;border-top:1px solid rgba(255,255,255,.25)}
.categories{margin-top:14px;border:1px solid var(--line)}
.categories .widget-head{background:var(--green)}
.categories ul{list-style:none;padding:4px 8px}
.categories li{font-size:6px;color:#666;padding:3px 0;border-bottom:1px solid var(--line);display:flex;gap:4px;align-items:center}
.categories li::before{content:"";width:3px;height:3px;background:var(--orange);border-radius:50%}
.ad{margin-top:16px;height:186px;position:relative;background:linear-gradient(160deg,#e9e2cf,#c8b88a 55%,#8a6a3a)}
.ad-copy{position:absolute;left:10px;bottom:24px;color:#5a3d1a}
.ad-copy .name{font-size:20px;font-weight:700}
.ad-copy .tag{font-size:9px}
.ad-sponsor{position:absolute;right:8px;bottom:6px;font-size:6px;color:var(--white)}

/* footer */
.footer{position:absolute;left:0;top:1062px;width:669px;height:138px;background:var(--green)}
.footer-cols{display:flex;padding:14px 73px 0;gap:22px}
.fcol h4{font-size:7px;color:var(--white);font-weight:700;margin-bottom:5px}
.fcol a{display:block;font-size:5.5px;color:#d8e8c8;text-decoration:none;line-height:9px}
.social{display:flex;gap:5px}
.social span{width:13px;height:13px;border-radius:50%;background:var(--social)}
.footer-bottom{position:absolute;bottom:0;width:100%;height:22px;background:var(--green-dark);font-size:5.5px;color:#cfe0c0;text-align:center;line-height:22px}
</style>
</head>
<body>
<div class="page">

<section class="hero">
  <div class="hero-photo" role="img" aria-label="Footballers challenging for the ball in a floodlit stadium"></div>
  <div class="topbar">
    <a>HOME</a><a>SPORT</a><a>FOOTBALL</a><a>BASKETBALL</a><a>TENNIS</a><a>CONTACT</a>
  </div>
  <header class="header">
    <div class="logo">Kickorra</div>
    <nav class="nav">
      <svg width="9" height="9" viewBox="0 0 10 10"><path d="M1 5 L5 1 L9 5 V9 H6 V6 H4 V9 H1Z" fill="#fff"/></svg>
      <a>LIVE</a><a>TOP MATCHES</a><a>SCORES UPDATE</a><a>NATIONS CUP</a><a>INTERNATIONAL</a><a>RESOURCES</a>
    </nav>
  </header>
  <div class="hero-copy">
    <div class="kicker">CHECK LIVE SCORE NOW</div>
    <h1>FINAL TOP MATCHES</h1>
    <span class="btn">VIEW SCORE</span>
  </div>
  <div class="hero-rule"></div>
</section>

<main class="main">
  <section class="scores">
    <h2 class="section-title">LATEST SCORES</h2>
    <div class="tabs">
      <span class="active">AUG 09</span><span>AUG 10</span><span>AUG 11</span><span>AUG 12</span><span>AUG 13</span><span>AUG 14</span><span>AUG 15</span><span>AUG 16</span>
    </div>

    <div class="group"><div class="league">Summit Games Women - 3rd place</div>
      <div class="match"><span>FT</span><span class="home">Sweden</span><span class="score">1 - 0</span><span>Germany</span><span></span></div></div>
    <div class="group"><div class="league">England - County Cup: qualification</div>
      <div class="match"><span>FT</span><span class="home">Hartley</span><span class="score">1 - 0</span><span>Brookfield</span><span></span></div></div>
    <div class="group-gap"></div>
    <div class="group"><div class="league">Summit Games Women - 3rd place</div>
      <div class="match"><span>FT</span><span class="home">Sweden</span><span class="score">1 - 0</span><span>Germany</span><span></span></div></div>
    <div class="group"><div class="league">England - County Cup: qualification</div>
      <div class="match"><span>FT</span><span class="home">Hartley</span><span class="score">1 - 0</span><span>Brookfield</span><span></span></div></div>
    <div class="group-gap"></div>
    <div class="group"><div class="league">Summit Games Women - 3rd place</div>
      <div class="match"><span>FT</span><span class="home">Sweden</span><span class="score">1 - 0</span><span>Germany</span><span></span></div></div>
    <div class="group"><div class="league">England - County Cup: qualification</div>
      <div class="match"><span>FT</span><span class="home">Hartley</span><span class="score">1 - 0</span><span>Brookfield</span><span></span></div></div>

    <div class="series">
      <div class="series-head">1ST SERIES TITLE</div>
      <div class="srow"><span>FT</span><span class="home">Ridge United</span><span class="score">2 - 1</span><span>Oakvale Rovers</span><span class="dot"></span></div>
      <div class="srow"><span>FT</span><span class="home">Lakeside City</span><span class="score">0 - 0</span><span>Millbrook Town</span><span class="dot"></span></div>
      <div class="srow"><span>FT</span><span class="home">Harbor Athletic</span><span class="score">3 - 2</span><span>Stonegate FC</span><span class="dot"></span></div>
      <div class="srow"><span>FT</span><span class="home">Pinewood</span><span class="score">1 - 1</span><span>Redcliff</span><span class="dot"></span></div>
      <div class="srow"><span>FT</span><span class="home">Northfield</span><span class="score">2 - 0</span><span>Westbury</span><span class="dot"></span></div>
      <div class="srow"><span>FT</span><span class="home">Elm Park</span><span class="score">0 - 1</span><span>Crown Albion</span><span class="dot"></span></div>
      <div class="srow"><span>FT</span><span class="home">Fairhaven</span><span class="score">4 - 1</span><span>Ashford Vale</span><span class="dot"></span></div>
      <div class="srow"><span>FT</span><span class="home">Kingsbridge</span><span class="score">1 - 2</span><span>Silverton</span><span class="dot"></span></div>
    </div>

    <div class="series" style="margin-top:6px">
      <div class="series-head">2ND SERIES TITLE</div>
      <div class="srow"><span>FT</span><span class="home">Ridge United</span><span class="score">1 - 0</span><span>Oakvale Rovers</span><span class="dot"></span></div>
      <div class="srow"><span>FT</span><span class="home">Lakeside City</span><span class="score">2 - 2</span><span>Millbrook Town</span><span class="dot"></span></div>
      <div class="srow"><span>FT</span><span class="home">Harbor Athletic</span><span class="score">0 - 3</span><span>Stonegate FC</span><span class="dot"></span></div>
      <div class="srow"><span>FT</span><span class="home">Pinewood</span><span class="score">1 - 0</span><span>Redcliff</span><span class="dot"></span></div>
      <div class="srow"><span>FT</span><span class="home">Northfield</span><span class="score">2 - 1</span><span>Westbury</span><span class="dot"></span></div>
      <div class="srow"><span>FT</span><span class="home">Elm Park</span><span class="score">3 - 3</span><span>Crown Albion</span><span class="dot"></span></div>
      <div class="srow"><span>FT</span><span class="home">Fairhaven</span><span class="score">0 - 1</span><span>Ashford Vale</span><span class="dot"></span></div>
    </div>

    <div class="more"><svg width="16" height="10" viewBox="0 0 16 10"><path d="M1 1 L8 8 L15 1" fill="none" stroke="#888" stroke-width="2"/></svg></div>
  </section>

  <aside class="sidebar">
    <div class="live-table">
      <div class="widget-head">LIVE SCORE TABLE</div>
      <div class="search">Select team</div>
      <div class="live-row"><span>Crest League</span><span>12</span></div>
      <div class="live-row"><span>Valley Cup</span><span>10</span></div>
      <div class="live-row"><span>Valley FC</span><span>9</span></div>
      <div class="live-row"><span>Harbor City</span><span>8</span></div>
      <div class="live-row"><span>Lakeside Town</span><span>7</span></div>
      <div class="live-row"><span>Ridge United</span><span>7</span></div>
      <div class="live-row"><span>Stonegate</span><span>6</span></div>
      <div class="live-row"><span>Millbrook Town</span><span>5</span></div>
      <div class="live-row"><span>Oakvale City</span><span>4</span></div>
      <div class="live-row"><span>Northfield</span><span>3</span></div>
      <div class="live-row"><span>Redcliff</span><span>2</span></div>
    </div>

    <div class="categories">
      <div class="widget-head">CATEGORIES</div>
      <ul>
        <li>Summit Games Men</li><li>Summit Games Women</li><li>Continental Cup</li><li>Nations Cup</li>
        <li>Nations Cup U21</li><li>Continental U21</li><li>Top Division</li><li>Second Division</li>
        <li>Nations Cup Women</li><li>Continental Women</li><li>Friendly</li><li>League Cup</li>
        <li>National</li><li>Others</li>
      </ul>
    </div>

    <div class="ad" role="img" aria-label="Charity advert with a warm illustrated home scene">
      <div class="ad-copy"><div class="name">HarborHome</div><div class="tag">Fresh Starts</div></div>
      <div class="ad-sponsor">proudly sponsored by Northgate</div>
    </div>
  </aside>
</main>

<footer class="footer">
  <div class="footer-cols">
    <div class="fcol"><h4>INFORMATION</h4><a>About us</a><a>Terms</a><a>Privacy policy</a><a>Help center</a><a>Adverts</a></div>
    <div class="fcol"><h4>FEATURED</h4><a>Top games</a><a>Contact</a><a>Partners</a><a>Live news</a><a>Blog</a></div>
    <div class="fcol"><h4>RESOURCES</h4><a>Live scores</a><a>Fixtures</a><a>Results</a><a>Tables</a></div>
    <div class="fcol"><h4>LINKS</h4><a>Top sports</a><a>Football news</a><a>Live results</a><a>Match centre</a></div>
    <div class="fcol"><h4>STAY IN TOUCH</h4><div class="social"><span></span><span></span><span></span><span></span><span></span></div></div>
  </div>
  <div class="footer-bottom">© 2016 Kickorra. All rights reserved. · pitchtally.example</div>
</footer>

</div>
</body>
</html>
```